Business Card for Language School (2 locations)

We need a sleek business card for a language school that is looking to update our image to be more professional. We work with students ages Pre-Kindergarten through adults. Our idea is to have an all-black business card with white or silver lettering. On the front will be the name of our school (Bright Meadow English Academy), and on the back there will be information for our location, phone number, email, and website (and possibly social media information). We have two school branches, so the address, phone number, and email address will be different for each branch, but all of the other information will stay the same. We'd like each branch to have a different color card edge that is neon. We are also open to suggestions and new ideas!

Some answers to questions we have received:
1. The reason we haven't added a logo is because we are looking to get a new one. We hadn't originally planned to do that at this time, but we are going to look into updating our project to include that as another aspect of it. We had previously planned to just include the school name on the front without a logo at this time.
2. We currently have two branches of our school, and we want our business card design to be uniform for each location. While it might make sense to put the information on one card right now, we plan to have more locations in the future, so we want to plan ahead with a unified design right now.
3. Our school addresses and phone numbers can be found on our website: www.brightmeadowlingo.example (at the bottom of the page)!
Updates

Part of this contest is also a new logo design. Our previous design was a train, which we would be open to keeping if it had an updated, sleeker design.

Contact Information for Business Card

Card #1:
Bright Meadow English Academy (Qinglu Branch)
Fuxing W. Rd. Sec. 3, Lane 412, No. 58, 1F
Beitou District, Taipei City 11260
02-2941-3086
qinglu@brightmeadowlingo.example

Card #2:
Bright Meadow English Academy (Heping Branch)
Linsen Road, No. 318, 1F
Songshan District, Taipei City 10587
02-2764-1520
heping@brightmeadowlingo.example

Both cards:
Website: www.brightmeadowlingo.example
Facebook: www.facebook.com/brightmeadowlingo
Instagram: @brightmeadowlingo

```html
<!DOCTYPE html>
<html lang="en">
<head>
<meta charset="utf-8">
<title>Bright Meadow English Academy – Business Card</title>
<link href="https://fonts.googleapis.com/css2?family=Roboto:wght@400;500;700&display=swap" rel="stylesheet">
<style>
  :root {
    --bg: #2a2a2a;
    --card: #151515;
    --silver: #c9c9c9;
    --ink: #f2f2f2;
    --rule: #bdbdbd;
  }
  * { box-sizing: border-box; margin: 0; padding: 0; }
  html, body { width: 1200px; height: 1200px; overflow: hidden; }
  body {
    background: var(--bg);
    font-family: "Roboto", Arial, sans-serif;
    color: var(--ink);
    position: relative;
  }
  .card {
    position: absolute;
    left: 170px;
    width: 860px;
    height: 480px;
    background: var(--card);
    box-shadow: 0 10px 30px rgba(0,0,0,.45);
  }
  .card--front { top: 110px; }
  .card--back { top: 620px; }

  .wordmark {
    font-weight: 500;
    color: var(--silver);
    text-transform: uppercase;
    line-height: 1;
  }
  .wordmark__main { display: block; font-size: 42px; letter-spacing: 1px; }
  .wordmark__sub { display: block; font-size: 22px; letter-spacing: 10px; margin-top: 6px; }

  .card--front .wordmark {
    position: absolute;
    top: 175px;
    left: 0; right: 0;
    text-align: center;
  }
  .card--front .website {
    position: absolute;
    bottom: 50px;
    left: 0; right: 0;
    text-align: center;
    font-size: 17px;
    letter-spacing: .5px;
  }

  .card--back .wordmark { position: absolute; top: 70px; left: 70px; }
  .card--back .rule {
    position: absolute;
    top: 215px; left: 70px; right: 70px;
    height: 1px;
    background: var(--rule);
  }
  .contacts {
    position: absolute;
    left: 70px; top: 250px;
    list-style: none;
    font-size: 19px;
  }
  .contacts li { display: flex; align-items: center; height: 33px; }
  .contacts svg, .contacts .mark {
    width: 20px; height: 20px; margin-right: 14px; flex: none;
  }
  .contacts .mark { border: 2px solid var(--ink); border-radius: 50%; width: 16px; height: 16px; margin: 0 16px 0 2px; }
  .branch {
    position: absolute;
    right: 70px; top: 300px;
    text-align: right;
    font-size: 19px;
    line-height: 1.35;
  }
  .branch__name { font-weight: 700; }
</style>
</head>
<body>
  <section class="card card--front">
    <div class="wordmark">
      <span class="wordmark__main">Bright Meadow</span>
      <span class="wordmark__sub">English Academy</span>
    </div>
    <p class="website">www.brightmeadowlingo.example</p>
  </section>

  <section class="card card--back">
    <div class="wordmark">
      <span class="wordmark__main">Bright Meadow</span>
      <span class="wordmark__sub">English Academy</span>
    </div>
    <div class="rule"></div>
    <ul class="contacts">
      <li>
        <svg viewBox="0 0 24 24" aria-hidden="true"><path fill="#f2f2f2" d="M6.6 10.8a15 15 0 0 0 6.6 6.6l2.2-2.2a1 1 0 0 1 1-.25 11.4 11.4 0 0 0 3.6.57 1 1 0 0 1 1 1V20a1 1 0 0 1-1 1A17 17 0 0 1 3 4a1 1 0 0 1 1-1h3.5a1 1 0 0 1 1 1c0 1.25.2 2.45.57 3.57a1 1 0 0 1-.25 1z"/></svg>
        02 2941 3086
      </li>
      <li>
        <svg viewBox="0 0 24 24" aria-hidden="true"><rect x="2" y="5" width="20" height="14" fill="none" stroke="#f2f2f2" stroke-width="2"/><path d="M2 5l10 8 10-8" fill="none" stroke="#f2f2f2" stroke-width="2"/></svg>
        qinglu@brightmeadowlingo.example
      </li>
      <li>
        <svg viewBox="0 0 24 24" aria-hidden="true" fill="none" stroke="#f2f2f2" stroke-width="1.6"><circle cx="12" cy="12" r="10"/><ellipse cx="12" cy="12" rx="4.5" ry="10"/><path d="M2 12h20M4 7h16M4 17h16"/></svg>
        www.brightmeadowlingo.example
      </li>
      <li><span class="mark"></span>brightmeadowlingo.example</li>
      <li><span class="mark"></span>@brightmeadowlingo</li>
    </ul>
    <address class="branch" style="font-style:normal">
      <div class="branch__name">Qinglu Branch</div>
      <div>No. 58, Lane 412, Section 3</div>
      <div>Fuxing West Road Beitou District</div>
      <div>Taipei City</div>
    </address>
  </section>
</body>
</html>
```